App Icon Designs

I am creating an app and I need icons for these categories:
Education
Entertainment
Finance
Games
Health & Fitness
Kids
Lifestyle
Medical
Music
Navigation
News
Photo & Video
Social Networking
Sports
Travel
Utilities
Weather
I would like the icon designs to imitate the style of the included picture. I have also included a picture of the buttons the icons should fit in (75 x 75 pixels). The icons should stick the the simple and flat look.
Please keep all icons 75 x 75 pixels, and NOT 90 x 90 pixels.
Prize increased to $230. Please do your best work. If anyone can successfully imitate the design of the picture included, I will be glad to increase the prize by another $100.

```html
<!DOCTYPE html>
<html lang="en">
<head>
<meta charset="utf-8">
<title>Discover</title>
<link rel="stylesheet" href="https://fonts.googleapis.com/css2?family=Nunito:wght@800;900&family=Roboto:wght@400;500&display=swap">
<style>
  :root {
    --page-bg: #e6f1f7;
    --bar-dark: #3b3b3b;
    --accent-line: #f26a50;
    --list-bg: #f2f2f2;
    --white: #ffffff;
    --tab-icon-dim: #9a9a9a;
    --photo: #02d382;
    --education: #2b91c6;
    --entertainment: #ee9335;
    --finance: #a15dbb;
    --games: #f8aa2a;
    --sports: #d2503a;
    --music: #01c6ad;
  }
  * { box-sizing: border-box; margin: 0; padding: 0; }
  html, body { width: 1200px; height: 1200px; overflow: hidden; }
  body { background: var(--page-bg); font-family: "Nunito", sans-serif; position: relative; }

  .screen { position: absolute; left: 269px; top: 0; width: 676px; height: 1200px; background: var(--list-bg); overflow: hidden; }

  .status-bar { position: absolute; left: 0; top: 0; width: 100%; height: 36px; background: var(--bar-dark);
    color: var(--white); font-family: "Roboto", sans-serif; font-size: 20px; }
  .status-carrier { position: absolute; left: 12px; top: 6px; letter-spacing: 0.3px; }
  .status-carrier .net { margin-left: 12px; }
  .status-time { position: absolute; left: 0; right: 0; top: 6px; text-align: center; font-weight: 500; }
  .status-battery { position: absolute; right: 12px; top: 6px; display: flex; align-items: center; gap: 8px; }

  .title-bar { position: absolute; left: 0; top: 36px; width: 100%; height: 79px; background: var(--bar-dark);
    color: var(--white); font-family: "Roboto", sans-serif; font-weight: 500; font-size: 30px;
    text-align: center; line-height: 78px; }
  .title-accent { position: absolute; left: 0; top: 115px; width: 100%; height: 8px; background: var(--accent-line); }

  .category-list { position: absolute; left: 23px; top: 136px; width: 630px; list-style: none; }
  .category { position: relative; height: 131px; margin-bottom: 13px; border-radius: 5px;
    box-shadow: inset 0 -3px 0 rgba(0,0,0,0.1); }
  .category-name { position: absolute; left: 0; right: 0; top: 0; height: 131px; line-height: 131px;
    text-align: center; color: var(--white); font-weight: 900; font-size: 31px; letter-spacing: 0.2px; }
  .category--photo .category-name { top: 3px; }
  .category--sports .category-name { top: 8px; }

  .category-art { position: absolute; }
  .art--camera { left: 33px; top: 17px; width: 131px; height: 96px; border-radius: 8px;
    background: linear-gradient(180deg, #a3a3a3 0 28%, #2aa8e0 28% 72%, #a3a3a3 72%); }
  .art--cap { left: 8px; top: 13px; width: 180px; height: 97px; border-radius: 40% 40% 30% 30%;
    background: linear-gradient(180deg, #2a2a2a, #5a5a5a); }
  .art--masks { left: 21px; top: 10px; width: 154px; height: 111px; border-radius: 20% 20% 45% 45%;
    background: linear-gradient(90deg, #f6c877, #f0b45a); }
  .art--pig { left: 33px; top: 9px; width: 125px; height: 113px; border-radius: 50%;
    background: radial-gradient(circle at 50% 45%, #f3c9ce, #e7a9b1); }
  .art--controller { left: 24px; top: 10px; width: 137px; height: 102px; border-radius: 30% 30% 40% 40%;
    background: linear-gradient(90deg, #927bb6, #7b5ea4); }
  .art--balls { left: 18px; top: 10px; width: 155px; height: 106px; border-radius: 50%;
    background: linear-gradient(90deg, #e9906a, #f3f3f3 45%, #3c4656 60%, #a55a3e); }
  .art--headphones { left: 31px; top: 5px; width: 112px; height: 105px; border-radius: 50% 50% 20% 20%;
    background: linear-gradient(180deg, #c8323a, #d9454a 60%, #3a3a3a); }

  .category--photo { background: var(--photo); }
  .category--education { background: var(--education); }
  .category--entertainment { background: var(--entertainment); }
  .category--finance { background: var(--finance); }
  .category--games { background: var(--games); }
  .category--sports { background: var(--sports); }
  .category--music { background: var(--music); }

  .tab-bar { position: absolute; left: 0; top: 1110px; width: 100%; height: 90px; background: var(--bar-dark); }
  .tab { position: absolute; top: 20px; width: 50px; height: 50px; }
  .tab--search { left: 88px; }
  .tab--feed { left: 313px; }
  .tab--profile { left: 538px; }
</style>
</head>
<body>
  <main class="screen">
    <header class="status-bar">
      <span class="status-carrier">●●●○○ Nimbus<span class="net">LTE</span></span>
      <span class="status-time">9:55 AM</span>
      <span class="status-battery">61%
        <svg width="44" height="18" viewBox="0 0 44 18" aria-hidden="true">
          <rect x="1" y="1" width="38" height="16" rx="3" fill="none" stroke="#fff" stroke-width="1.5"/>
          <rect x="3.5" y="3.5" width="21" height="11" rx="1.5" fill="#fff"/>
          <rect x="40.5" y="6" width="2.5" height="6" rx="1" fill="#fff"/>
        </svg>
      </span>
    </header>
    <div class="title-bar">Discover</div>
    <div class="title-accent"></div>

    <ul class="category-list">
      <li class="category category--photo">
        <div class="category-art art--camera" role="img" aria-label="Flat grey and blue camera icon"></div>
        <span class="category-name">Photo &amp; Video</span>
      </li>
      <li class="category category--education">
        <div class="category-art art--cap" role="img" aria-label="Flat black graduation cap icon with gold tassel"></div>
        <span class="category-name">Education</span>
      </li>
      <li class="category category--entertainment">
        <div class="category-art art--masks" role="img" aria-label="Flat pale yellow theatre masks icon"></div>
        <span class="category-name">Entertainment</span>
      </li>
      <li class="category category--finance">
        <div class="category-art art--pig" role="img" aria-label="Flat pink piggy bank icon with coin"></div>
        <span class="category-name">Finance</span>
      </li>
      <li class="category category--games">
        <div class="category-art art--controller" role="img" aria-label="Flat purple game controller icon"></div>
        <span class="category-name">Games</span>
      </li>
      <li class="category category--sports">
        <div class="category-art art--balls" role="img" aria-label="Flat basketball, soccer ball and football icon"></div>
        <span class="category-name">Sports</span>
      </li>
      <li class="category category--music">
        <div class="category-art art--headphones" role="img" aria-label="Flat red headphones icon"></div>
        <span class="category-name">Music</span>
      </li>
    </ul>

    <nav class="tab-bar">
      <svg class="tab tab--search" viewBox="0 0 50 50" aria-label="Search">
        <circle cx="21" cy="21" r="14" fill="none" stroke="var(--white)" stroke-width="5"/>
        <line x1="31" y1="31" x2="44" y2="44" stroke="var(--white)" stroke-width="6" stroke-linecap="round"/>
      </svg>
      <svg class="tab tab--feed" viewBox="0 0 50 50" aria-label="Feed">
        <path d="M4 30 A22 22 0 0 1 46 30" fill="none" stroke="var(--tab-icon-dim)" stroke-width="7"/>
        <circle cx="25" cy="36" r="6" fill="var(--tab-icon-dim)"/>
      </svg>
      <svg class="tab tab--profile" viewBox="0 0 50 50" aria-label="Profile">
        <rect x="17" y="2" width="16" height="24" rx="8" fill="var(--tab-icon-dim)"/>
        <path d="M2 48 V40 Q2 32 12 31 H38 Q48 32 48 40 V48 Z" fill="var(--tab-icon-dim)"/>
      </svg>
    </nav>
  </main>
</body>
</html>
```